Outdoor paradise advertisement

This will be a full-page advertisement in Pine Porch Journal (North Carolina, USA). We want to promote our community as an Outdoor Paradise. We are a rural community and water sports are a big part of our offerings. I will attach a few photo but all do not have to be included.

Full page: 8.25" x 10.875"
+.125" bleed all sides; safety from trim: .5"

Marlowe Chamber of Commerce and Tourism
438 North Tilden Avenue, Whiteville, NC 28519
(910) 555-0187
www.TheMarloweChamber.example

Target Market(s)

Travelers who enjoy watersports, outdoor enthusiasts.

Font styles to use
Serif
Sans Serif

Requirements
Must have
• An outdoorsy feel, one or more images, our logo and contact information, and a call to action, Explore Marlowe County, NC.
Nice to have
• Bullets or reference to some of our attractions
Agritourism
Arts/Cultural
Camping
Canoeing/Kayaking
Fishing
Golf
Historic Sites
Horses
Museums
Sports & Recreation
Outdoor Activities
Zoo
Should not have
• Anything that looks too metropolitian.

```html
<!DOCTYPE html>
<html lang="en">
<head>
<meta charset="utf-8">
<title>Explore Marlowe County, NC</title>
<link rel="stylesheet" href="https://fonts.googleapis.com/css2?family=Caveat+Brush&family=Cinzel:wght@400&family=Didact+Gothic&family=Archivo:wght@800&display=swap">
<style>
  :root {
    --sky-top: #4a86bd;
    --sky-mid: #7ea6cf;
    --mist: #f6f8ee;
    --band-blue: #0a98dc;
    --navy: #22307a;
    --ink: #1f2a33;
    --white: #ffffff;
    --logo-blue: #2a3d8f;
  }
  html, body { margin: 0; padding: 0; overflow: hidden; }
  body { width: 921px; height: 1200px; }
  .ad {
    position: relative;
    width: 921px;
    height: 1200px;
    overflow: hidden;
    background:
      radial-gradient(ellipse 700px 360px at 40% 870px, rgba(250,250,235,0.95), rgba(250,250,235,0) 70%),
      linear-gradient(180deg, var(--sky-top) 0%, #5790c4 40%, var(--sky-mid) 62%, var(--mist) 88%, var(--white) 100%);
    font-family: "Didact Gothic", sans-serif;
    color: var(--ink);
  }
  .headline {
    position: absolute;
    right: 52px;
    top: 40px;
    margin: 0;
    text-align: right;
    color: var(--white);
    font-weight: 400;
  }
  .headline-word {
    display: block;
    font-family: "Caveat Brush", cursive;
    font-size: 150px;
    line-height: 1;
    letter-spacing: 1px;
  }
  .headline-place {
    display: block;
    margin-top: 6px;
    font-family: "Cinzel", serif;
    font-size: 29px;
    letter-spacing: 1.5px;
  }
  .photo-pages { position: absolute; left: 0; top: 0; width: 921px; height: 960px; }
  .attractions {
    position: absolute;
    left: 44px;
    top: 826px;
    display: grid;
    grid-template-columns: 242px 260px;
    grid-auto-flow: column;
    grid-template-rows: repeat(6, 31px);
    margin: 0; padding: 0;
    list-style: none;
    font-size: 21px;
    line-height: 31px;
    color: var(--ink);
  }
  .contact-band {
    position: absolute;
    left: 0; top: 1049px;
    width: 921px; height: 151px;
  }
  .brand {
    position: absolute;
    left: 50px;
    top: 1108px;
    display: flex;
    align-items: center;
    gap: 10px;
    font-family: "Didact Gothic", sans-serif;
    font-size: 18px;
    line-height: 1.2;
    letter-spacing: 1.5px;
    text-transform: uppercase;
    color: var(--logo-blue);
  }
  .brand-dot { width: 18px; height: 18px; border-radius: 50%; background: var(--logo-blue); flex: none; }
  .contact {
    position: absolute;
    right: 52px;
    top: 1060px;
    text-align: right;
    color: var(--white);
    font-style: normal;
  }
  .contact-name { display: block; font-size: 25px; line-height: 1.2; }
  .contact-address { display: block; font-size: 15.5px; line-height: 1.3; }
  .contact-phone {
    display: block;
    font-family: "Archivo", sans-serif;
    font-weight: 800;
    font-size: 37px;
    line-height: 1.05;
    color: var(--navy);
    margin-top: 2px;
  }
  .contact-web { display: block; font-size: 17.5px; line-height: 1.35; letter-spacing: 0.3px; }
</style>
</head>
<body>
<main class="ad">
  <svg class="photo-pages" viewBox="0 0 921 960">
    <defs>
      <linearGradient id="sail-tones" x1="0" y1="0" x2="0" y2="1">
        <stop offset="0" stop-color="#4f86c4"/>
        <stop offset="0.35" stop-color="#8fb1d8"/>
        <stop offset="0.55" stop-color="#dfe7ef"/>
        <stop offset="0.72" stop-color="#7c98bd"/>
        <stop offset="0.85" stop-color="#3f5f8e"/>
        <stop offset="1" stop-color="#2a4676"/>
      </linearGradient>
      <linearGradient id="golf-tones" x1="0" y1="0" x2="0" y2="1">
        <stop offset="0" stop-color="#f1f3ee"/>
        <stop offset="0.22" stop-color="#c9d6c0"/>
        <stop offset="0.36" stop-color="#5e8548"/>
        <stop offset="0.5" stop-color="#47703a"/>
        <stop offset="0.62" stop-color="#93b25c"/>
        <stop offset="1" stop-color="#a8c46c"/>
      </linearGradient>
      <filter id="page-shadow" x="-10%" y="-10%" width="130%" height="130%">
        <feDropShadow dx="4" dy="10" stdDeviation="10" flood-color="#23324a" flood-opacity="0.28"/>
      </filter>
    </defs>
    <path role="img" aria-label="Photo: sailboat with white sails on open water under a blue sky"
          d="M596 330 Q760 300 921 366 L921 930 L870 937 Q680 900 461 850 Z"
          fill="url(#sail-tones)" filter="url(#page-shadow)"/>
    <path role="img" aria-label="Photo: golfer teeing off on a green fairway lined with pine trees"
          d="M238 122 Q470 150 596 316 Q540 600 461 852 Q280 730 84 710 Q150 420 238 122 Z"
          fill="url(#golf-tones)" filter="url(#page-shadow)"/>
  </svg>

  <h1 class="headline">
    <span class="headline-word">Explore</span>
    <span class="headline-place">Marlowe County, NC.</span>
  </h1>

  <ul class="attractions">
    <li>Historic Sites</li>
    <li>Museums</li>
    <li>Outdoor Activities</li>
    <li>Agritourism</li>
    <li>Camping</li>
    <li>Fishing</li>
    <li>Horses</li>
    <li>Sports &amp; Recreation</li>
    <li>Zoo</li>
    <li>Arts/Cultural</li>
    <li>Canoeing/Kayaking</li>
    <li>Golf</li>
  </ul>

  <svg class="contact-band" viewBox="0 0 921 151" aria-hidden="true">
    <rect x="0" y="0" width="921" height="151" fill="var(--band-blue)"/>
    <path d="M0 0 L273 0 Q350 20 376 151 L0 151 Z" fill="var(--white)"/>
  </svg>

  <div class="brand">
    <span class="brand-dot"></span>
    <span>Marlowe Chamber<br>of Commerce &amp; Tourism</span>
  </div>

  <address class="contact">
    <span class="contact-name">Marlowe Chamber of Commerce and Tourism</span>
    <span class="contact-address">438 North Tilden Avenue, Whiteville, NC 28519</span>
    <span class="contact-phone">(910) 555-0187</span>
    <span class="contact-web">www.TheMarloweChamber.example</span>
  </address>
</main>
</body>
</html>
```